Modern Label for cleaning products for the brand Dorvalix

We need a label design for our line of cleaning products. The label should feature our logo and an image to identify the product's intended use. I've added our logo and an image for use. This only concerns the design of the label on the front of the bottle.

Label dimensions:
Label 1 (500ml bottle with spray): width 58mm x height 115mm
Label 2: (1L bottle): width 73mm x height 140mm
The design must be consistent for both bottles which you find in the pictures.

The bottles to be labeled are white. See the attachment for a photo of the bottles.

The photo must also appear on the label to identify the product's intended use.

Product information:
Brand: Dorvalix
Product: Sanitary Cleaner

This text must be placed on the label:
"Cleans, descales & freshens. followed with this text: "Ideal for quick and powerful cleaning. A ready-to-use product for everyday use."

- Mention the seperate USP's: Sanitary, Bathroom, Toilet, Wet areas

Appearance: This is a consumer product, but it must have a professional appearance. We would like to see a design that use the color blue from our logo.

Target Market(s)

Consumers who take care of their homes and want to maintain it the correct (professional) way

Font styles to use
Sans Serif

Colors
0054AA
0677BA
7BADD7
CADEEF
E8F1F8

Requirements
Must have
• USP's + use of image and logo + blend in 1 design
Nice to have
• Keep the color of the logo in the design
Should not have
• Comic sans

```html
<!DOCTYPE html>
<html lang="en">
<head>
<meta charset="utf-8">
<title>Dorvalix Sanitary Spray Cleaner Labels</title>
<link rel="stylesheet" href="https://fonts.googleapis.com/css2?family=Barlow:wght@500;600;700&display=swap">
<style>
  :root{
    --blue-deep:#0054AA;
    --blue-mid:#0677BA;
    --blue-light:#7BADD7;
    --blue-pale:#CADEEF;
    --blue-mist:#E8F1F8;
    --canvas:#e6e6e6;
    --ink:#1c1c1c;
    --title-ink:#e4eaf0;
    --white:#ffffff;
  }
  *{margin:0;padding:0;box-sizing:border-box}
  html,body{width:1109px;height:1200px;overflow:hidden;background:var(--canvas)}
  body{position:relative;font-family:"Barlow",Arial,sans-serif}
  .label{position:absolute;background:var(--white);overflow:hidden;box-shadow:4px 4px 6px rgba(0,0,0,.28)}
  .label--500{left:98px;top:309px;width:366px;height:725px}
  .label--1000{left:541px;top:152px;width:461px;height:882px}

  .brand{position:absolute;left:0;width:100%;display:flex;flex-direction:column;align-items:center}
  .brand__dot{border-radius:50%;background:var(--blue-mid)}
  .brand__name{font-weight:700;color:var(--ink);letter-spacing:.5px;line-height:1}

  .title-band{position:absolute;left:0;width:100%;display:flex;align-items:center;justify-content:center;
    background:linear-gradient(90deg,var(--blue-deep),var(--blue-mid) 60%,#1a8bd0);
    color:var(--title-ink);font-weight:600;letter-spacing:1px;text-shadow:0 1px 2px rgba(0,0,0,.25)}

  .scene{position:absolute;left:0;width:100%;
    background:linear-gradient(180deg,#e9ebed 0%,#b8b6b3 35%,#d8d9da 60%,#a9a6a2 100%)}

  .info{position:absolute;left:0;width:100%;bottom:0;
    background:linear-gradient(120deg,var(--blue-deep) 0%,var(--blue-mid) 55%,#1991d2 100%);color:var(--white)}

  .usp{position:absolute;list-style:none;background:rgba(110,175,225,.6);color:var(--white);font-weight:600;z-index:2}
  .usp li::before{content:"• "}

  .rule{position:absolute;height:2px;background:#b7cde0}
  .tagline{position:absolute;left:0;width:100%;text-align:center;color:var(--blue-pale);font-weight:600;letter-spacing:.5px}
  .blurb{position:absolute;left:0;width:100%;text-align:center;font-weight:600;line-height:1.4}
  .volume{position:absolute;left:0;width:100%;text-align:center;font-weight:600}

  /* 500ml */
  .label--500 .brand{top:42px}
  .label--500 .brand__dot{width:40px;height:40px;margin-bottom:14px}
  .label--500 .brand__name{font-size:32px}
  .label--500 .title-band{top:160px;height:57px;font-size:24px}
  .label--500 .scene{top:217px;height:360px}
  .label--500 .info{height:148px}
  .label--500 .usp{left:26px;top:456px;width:136px;height:137px;padding:14px 0 0 18px;font-size:17px;line-height:25.5px}
  .label--500 .rule{left:26px;right:26px}
  .label--500 .rule--top{top:30px}
  .label--500 .rule--bottom{top:63px}
  .label--500 .tagline{top:36px;font-size:19px}
  .label--500 .blurb{top:75px;font-size:11px}
  .label--500 .volume{top:125px;font-size:11.5px}

  /* 1000ml */
  .label--1000 .brand{top:52px}
  .label--1000 .brand__dot{width:50px;height:50px;margin-bottom:18px}
  .label--1000 .brand__name{font-size:40px}
  .label--1000 .title-band{top:192px;height:72px;font-size:30px}
  .label--1000 .scene{top:264px;height:431px}
  .label--1000 .info{height:187px}
  .label--1000 .usp{left:40px;top:549px;width:166px;height:166px;padding:16px 0 0 20px;font-size:21.5px;line-height:31px}
  .label--1000 .rule{left:40px;right:40px}
  .label--1000 .rule--top{top:42px}
  .label--1000 .rule--bottom{top:82px}
  .label--1000 .tagline{top:48px;font-size:23px}
  .label--1000 .blurb{top:95px;font-size:13px}
  .label--1000 .volume{top:156px;font-size:14px}
</style>
</head>
<body>

<article class="label label--500">
  <div class="brand"><span class="brand__dot"></span><span class="brand__name">Dorvalix</span></div>
  <div class="title-band">SANITARY SPRAY CLEANER</div>
  <div class="scene" role="img" aria-label="Photo of a modern bathroom with glass shower, white vanity and grey tiles"></div>
  <ul class="usp"><li>Sanitary</li><li>Bathroom</li><li>Toilet</li><li>Wet areas</li></ul>
  <section class="info">
    <div class="rule rule--top"></div>
    <p class="tagline">Cleans, descales &amp; freshens.</p>
    <div class="rule rule--bottom"></div>
    <p class="blurb">Ideal for quick and powerful cleaning.<br>A ready-to-use product for everyday use.</p>
    <p class="volume">500ml</p>
  </section>
</article>

<article class="label label--1000">
  <div class="brand"><span class="brand__dot"></span><span class="brand__name">Dorvalix</span></div>
  <div class="title-band">SANITARY SPRAY CLEANER</div>
  <div class="scene" role="img" aria-label="Photo of a modern bathroom with glass shower, white vanity and grey tiles"></div>
  <ul class="usp"><li>Sanitary</li><li>Bathroom</li><li>Toilet</li><li>Wet areas</li></ul>
  <section class="info">
    <div class="rule rule--top"></div>
    <p class="tagline">Cleans, descales &amp; freshens.</p>
    <div class="rule rule--bottom"></div>
    <p class="blurb">Ideal for quick and powerful cleaning.<br>A ready-to-use product for everyday use.</p>
    <p class="volume">1000ml</p>
  </section>
</article>

</body>
</html>
```